Gravelcraft Lip Balm. It is formulated with men in mind but other people certainly can use it.

The over arching name of the project is Tuskwell - which needs to be in the label somewhere, but Gravelcraft is the title.
It would be for a round jar container.
It is out of promoting products for men to open discussion about health issues that men often not talk about. As each product is created it will have a message to men about the health issue and where to find information, seek help or just be able to talk about it.
I would like darker colours (black) as the base but using other colours to
for the wording and design.
I am open to ideas on the layout, I have included some ideas, and also some of my own labelling ideas that I have worked on. I do like the carbon fibre background look that I have for my tusker label. I have also included my Keelward label with some colour ideas.
I also was wondering about making it a after tattoo balm so that it can also be used as a lip balm as well…two for the price of one..basically the same ingredients are used.
They may change the look of the intended artwork..but I leave it in your skill full hands.
My number is +61490218537. You can txt me if you need some clarification.
Thank you
Kind regards and blessings

Target Market(s)

Target market is men of all ages as they can all be affected by one health issue or another at different times of life

Industry/Entity Type

Healthcare and beauty

Font styles to use
Sans Serif
Decorative

Requirements
Must have
• I still need to indeed to ingredients and container size.
Nice to have
• A novel and different look from the usual crowd that try to hard to look cool or funky

```html
<!DOCTYPE html>
<html lang="en">
<head>
<meta charset="utf-8">
<title>Tuskwell – Gravelcraft Lip Balm Label</title>
<link href="https://fonts.googleapis.com/css2?family=Great+Vibes&family=Quicksand:wght@500;600&family=Baloo+2:wght@700&family=Cormorant+Garamond:wght@500&display=swap" rel="stylesheet">
<style>
  :root {
    --bg: #ebebeb;
    --jar-black: #161616;
    --carbon-dark: #1c1c1c;
    --carbon-light: #2e2e2e;
    --silver: #c9c9c9;
    --ink-white: #f2f2f2;
    --brand-green: #8cd62a;
    --tag-grey: #cfcfcf;
    --balm-red: #8e1526;
    --balm-red-soft: #b0203a;
    --balm-text: #f4e9ea;
    --fine-print: #bdbdbd;
  }
  * { margin: 0; padding: 0; box-sizing: border-box; }
  html, body { width: 1200px; height: 1200px; overflow: hidden; }
  body {
    background: var(--bg);
    display: flex;
    flex-direction: column;
    align-items: center;
    justify-content: center;
    gap: 60px;
  }

  /* Lid artwork */
  .lid {
    position: relative;
    width: 440px;
    height: 440px;
    border-radius: 50%;
    border: 6px solid var(--jar-black);
    overflow: hidden;
  }
  .carbon-texture {
    position: absolute;
    inset: 0;
    background: radial-gradient(circle at 40% 35%, var(--carbon-light), var(--carbon-dark) 75%);
  }
  .lid-brand {
    position: absolute;
    inset: 0;
    display: flex;
    flex-direction: column;
    align-items: center;
    justify-content: center;
    gap: 14px;
  }
  .brand-name {
    font-family: "Quicksand", sans-serif;
    font-weight: 600;
    font-size: 58px;
    line-height: 1;
    color: var(--brand-green);
  }
  .brand-tagline {
    font-family: "Quicksand", sans-serif;
    font-weight: 500;
    font-size: 20px;
    letter-spacing: 3px;
    text-transform: uppercase;
    color: var(--tag-grey);
  }

  /* Side wrap label */
  .side-label {
    position: relative;
    width: 1080px;
    height: 380px;
    border-radius: 8px;
    overflow: hidden;
    border-top: 6px solid var(--silver);
  }
  .side-label .carbon-texture {
    background: linear-gradient(90deg, var(--carbon-dark), var(--carbon-light) 50%, var(--carbon-dark));
  }
  .label-content {
    position: absolute;
    inset: 0;
    display: flex;
    flex-direction: column;
    align-items: center;
    justify-content: center;
  }
  .range-name {
    font-family: "Great Vibes", cursive;
    font-size: 44px;
    line-height: 1;
    color: var(--ink-white);
  }
  .product-title {
    font-family: "Great Vibes", cursive;
    font-weight: 400;
    font-size: 140px;
    line-height: 1.05;
    color: var(--ink-white);
  }
  .product-type {
    position: relative;
    margin-top: 4px;
    padding: 2px 70px;
  }
  .brush-swatch {
    position: absolute;
    inset: 0;
    border-radius: 6px;
    background: linear-gradient(90deg, transparent, var(--balm-red) 15%, var(--balm-red-soft) 60%, var(--balm-red) 85%, transparent);
  }
  .product-type-text {
    position: relative;
    font-family: "Baloo 2", sans-serif;
    font-weight: 700;
    font-size: 46px;
    line-height: 1.3;
    color: var(--balm-text);
  }
  .net-weight {
    margin-top: 16px;
    font-family: "Cormorant Garamond", serif;
    font-weight: 500;
    font-size: 18px;
    color: var(--fine-print);
  }
</style>
</head>
<body>

  <section class="lid">
    <div class="carbon-texture" role="img" aria-label="Dark carbon fibre hexagon texture"></div>
    <div class="lid-brand">
      <p class="brand-name">Keelward</p>
      <p class="brand-tagline">Head, Heart &amp; Health</p>
    </div>
  </section>

  <section class="side-label">
    <div class="carbon-texture" role="img" aria-label="Dark carbon fibre hexagon texture"></div>
    <div class="label-content">
      <p class="range-name">Tuskwell</p>
      <h1 class="product-title">Gravelcraft</h1>
      <div class="product-type">
        <div class="brush-swatch" role="img" aria-label="Red brush stroke behind product name"></div>
        <span class="product-type-text">Lip Balm</span>
      </div>
      <p class="net-weight">Net Wt. 20 g</p>
    </div>
  </section>

</body>
</html>
```